The Marigold Nook

I need a website design for my business in Ontario, Canada. I am a Bowen Therapist, Calvera Method Practitioner and Reiki Practitioner for People and animals. I want my website to convey a sense of connection, energy, and harmony which will align with my work in Bowen Therapy, Reiki, and Calvera Method Fork Therapy. I will be offering these services as well as downloadable audio files, subscriptions and online courses. I want the website to be simple, elegant and professional and most of all to be memorable. I treat animals as well so would like an aspect of this in the logo without looking cheesy. I want the logo to convey a sense of community for both online and in-person events. I want it to be appealing and approachable to those both familiar and unfamiliar with holistic modalities. I will be adding Nutrition, Iridology and herbal supports as services as well later into my journey.

Target Market(s)

Animal healing clients Pet Owners (older pets, stressed/anxious pets, recovering from surgery or injury) Holistic & Natural Pet Care Enthusiasts Working animals (show/agility competitors/breeders) Human healing clients – people dealing with musculoskeletal pain, mobility issues, chronic pain, stress & anxiety, PTSD, people already interested in holistic and alternative health practitioners, Athletes and performers looking to optimize function and recover, Courses People interested in learning for themselves and pets Audio files People interested in helping themselves and their pets

Industry/Entity Type

Holistic Wellness

Requirements
Should not have
• cluttered design, annoying pop ups, poor mobility experience

```html
<!DOCTYPE html>
<html lang="en">
<head>
<meta charset="utf-8">
<title>The Marigold Nook</title>
<link href="https://fonts.googleapis.com/css2?family=Montserrat:wght@400;500;600;700;800&family=Roboto:wght@400;500&display=swap" rel="stylesheet">
<style>
:root{
  --green-dark:#0d5a34;
  --green:#1f7a3c;
  --green-light:#6dbb3a;
  --ink:#111;
  --body:#444;
  --hero:#0c3a2e;
  --mint:#e8f0ec;
  --cream:#f7f4ee;
  --white:#fff;
  --black:#000;
  --star:#f5a623;
}
*{margin:0;padding:0;box-sizing:border-box}
html,body{width:1200px;height:3627px;overflow:hidden}
body{font-family:"Montserrat",sans-serif;color:var(--ink);background:var(--white);position:relative}
.abs{position:absolute}
.btn{position:absolute;display:flex;align-items:center;justify-content:center;border-radius:30px;color:var(--white);font-weight:700;font-size:15px;background:linear-gradient(90deg,var(--green-light),var(--green-dark))}
.heading{position:absolute;left:0;width:1200px;text-align:center;font-weight:700;font-size:31px}
.heading::after{content:"";display:block;width:50px;height:3px;background:var(--green-dark);margin:14px auto 0}

/* header */
.header{position:absolute;top:0;left:0;width:1200px;height:112px}
.logo{position:absolute;left:111px;top:8px;width:156px;text-align:center}
.logo-mark{width:50px;height:50px;border-radius:50%;background:var(--green-light);margin:0 auto 6px}
.logo-name{font-weight:700;font-size:16px;line-height:23px;color:var(--ink)}
.nav{position:absolute;top:46px;left:447px;display:flex;gap:29px;font-size:15px;font-weight:500}
.nav .active{color:var(--green-dark);text-decoration:underline;text-underline-offset:5px;font-weight:700}

/* hero */
.hero{position:absolute;top:112px;left:0;width:1200px;height:547px;border-radius:30px;background:radial-gradient(ellipse at 40% 10%,#3f7a50 0%,#174d38 35%,var(--hero) 75%)}
.hero h1{position:absolute;left:111px;top:148px;font-size:47px;line-height:62px;color:var(--white);font-weight:700}
.hero p{position:absolute;left:111px;top:272px;width:480px;font-size:15px;line-height:29px;color:var(--white)}
.hero-photo{position:absolute;left:638px;top:65px;width:450px;height:416px;border-radius:24px;background:linear-gradient(160deg,#f4f1ec,#d9d3c9 60%,#9bb2cf)}

/* services */
.services{position:absolute;top:659px;left:0;width:1200px;height:580px;background:linear-gradient(180deg,#f6f6f4,#f2ede6 70%,#faf7f2)}
.svc-card{position:absolute;top:218px;width:304px;height:253px;background:var(--white);border-radius:12px;box-shadow:0 4px 16px rgba(0,0,0,.07);text-align:center}
.svc-icon{position:absolute;left:100px;top:-50px;width:104px;height:104px;border-radius:50%;border:2px solid var(--green);background:var(--white);display:flex;align-items:center;justify-content:center}
.svc-icon span{width:86px;height:86px;border-radius:50%;background:var(--green-dark);display:flex;align-items:center;justify-content:center}
.svc-card.mid .svc-icon span{background:linear-gradient(135deg,var(--green-light),var(--green))}
.svc-card h3{position:absolute;top:82px;width:100%;font-size:19px;font-weight:700}
.svc-card p{position:absolute;top:113px;left:22px;right:22px;font-size:14px;line-height:26px;color:var(--body)}
.read-link{position:absolute;top:203px;width:100%;font-size:13px;font-weight:700;color:var(--green-dark)}

/* about */
.about{position:absolute;top:1239px;left:0;width:1200px;height:567px;background:linear-gradient(90deg,#e3ece8,#edf2ef 50%,#e8efeb)}
.about-ring{position:absolute;left:165px;top:87px;width:386px;height:386px;border-radius:50%;border:3px solid var(--green-light)}
.about-photo{position:absolute;left:178px;top:100px;width:360px;height:360px;border-radius:50%;border:4px solid var(--green);background:radial-gradient(circle at 55% 40%,#e8c38f,#b7874f 55%,#8a6f3e)}
.about h2{position:absolute;left:632px;top:91px;font-size:31px;font-weight:700}
.about p{position:absolute;left:632px;width:460px;font-size:14px;line-height:29px;color:var(--body)}

/* works */
.works{position:absolute;top:1806px;left:0;width:1200px;height:775px;background:linear-gradient(180deg,#faf7f2,#f7efe4 60%,#f3ead9)}
.work-card{position:absolute;width:304px;background:var(--white);border-radius:12px;box-shadow:0 4px 16px rgba(0,0,0,.07);text-align:center}
.work-img{position:absolute;left:19px;top:20px;width:266px;height:193px;border-radius:10px}
.work-card h3{position:absolute;top:230px;width:100%;font-size:19px;font-weight:700;line-height:30px}
.work-card p{position:absolute;left:16px;right:16px;font-size:14px;line-height:26px;color:var(--body)}
.dots{position:absolute;background-image:radial-gradient(#999 1.3px,transparent 1.4px);background-size:11px 11px}

/* testimonials */
.testimonials{position:absolute;top:2581px;left:0;width:1200px;height:619px;background:linear-gradient(180deg,#e6efeb,#eef3f0)}
.testimonials .heading{font-size:31px;letter-spacing:.5px}
.t-card{position:absolute;top:180px;width:307px;height:327px;background:var(--white);border-radius:12px;box-shadow:0 4px 16px rgba(0,0,0,.07);font-family:"Roboto",sans-serif}
.stars{position:absolute;left:26px;top:30px;display:flex;gap:3px}
.t-card p{position:absolute;left:26px;right:26px;top:52px;font-size:13.5px;line-height:25.5px;color:#333;text-align:justify}
.t-rule{position:absolute;left:26px;right:26px;top:216px;height:2px;background:#bbb}
.avatar{position:absolute;left:26px;top:241px;width:54px;height:54px;border-radius:50%;background:linear-gradient(135deg,#c9c9c9,#8d9aa6)}
.t-name{position:absolute;left:100px;top:246px;font-size:18px;font-weight:500;color:var(--ink)}
.t-loc{position:absolute;left:98px;top:274px;font-size:14px;color:#333}
.arrow-btn{position:absolute;width:38px;height:38px;border-radius:50%;border:1.5px solid var(--green);display:flex;align-items:center;justify-content:center}

/* footer */
.footer{position:absolute;top:3200px;left:0;width:1200px;height:427px;background:var(--black);color:var(--white)}
.footer h4{position:absolute;top:61px;font-size:20px;font-weight:600}
.f-list{position:absolute;top:103px;list-style:none;font-size:15px;line-height:31px}
.f-list li{display:flex;align-items:center;gap:12px}
.f-contact{position:absolute;left:507px;display:flex;align-items:center;gap:13px;font-size:15px;line-height:20px}
.f-ico{width:38px;height:38px;border-radius:50%;background:var(--white);display:flex;align-items:center;justify-content:center;flex:none}
.news p{position:absolute;left:812px;top:110px;width:290px;font-size:14.5px;line-height:31px}
.email-field{position:absolute;left:814px;top:185px;width:270px;height:40px;border-bottom:2px solid var(--white);font-size:15px;padding-top:8px}
.subscribe{position:absolute;left:818px;top:243px;width:146px;height:50px;border-radius:26px;background:var(--white);color:var(--ink);font-weight:600;font-size:17px;display:flex;align-items:center;justify-content:center}
.f-rule{position:absolute;left:98px;top:365px;width:1003px;height:1px;background:#666}
.copyright{position:absolute;top:389px;width:1200px;text-align:center;font-size:14.5px}
</style>
</head>
<body>

<header class="header">
  <div class="logo">
    <div class="logo-mark"></div>
    <div class="logo-name">THE MARIGOLD NOOK</div>
  </div>
  <nav class="nav">
    <span class="active">Home</span><span>About Us</span><span>Services</span><span>Our Works</span><span>Testimonials</span>
  </nav>
  <div class="btn" style="left:956px;top:34px;width:132px;height:46px;font-size:16px">Contact Us</div>
</header>

<section class="hero">
  <h1>Welcome To<br>The Marigold Nook</h1>
  <p>Lorem ipsum dolor sit amet, consectetur adipiscing elit, sed do eiusmod tempor incididunt ut labore et dolore magna aliqua.</p>
  <div class="btn" style="left:111px;top:346px;width:133px;height:44px">Get Started</div>
  <div class="hero-photo" role="img" aria-label="Therapist seated on the floor of a bright room with a small white dog"></div>
</section>

<section class="services">
  <h2 class="heading" style="top:81px">Our Services</h2>

  <div class="svc-card" style="left:111px">
    <div class="svc-icon"><span>
      <svg width="34" height="34" viewBox="0 0 24 24" fill="none" stroke="#fff" stroke-width="1.8"><path d="M6 2h9l4 4v16H6z" fill="#fff" stroke="none"/><path d="M9 11v4h2l3 3V8l-3 3z" fill="#0d5a34" stroke="none"/><path d="M16 10.5a3 3 0 0 1 0 5" stroke="#0d5a34"/></svg>
    </span></div>
    <h3>Audio Files</h3>
    <p>Lorem ipsum dolor sit amet, consectetur adipiscing elit, sed do et dolore magna aliqua.</p>
    <div class="read-link">Read More &#10140;</div>
  </div>

  <div class="svc-card mid" style="left:448px">
    <div class="svc-icon"><span>
      <svg width="36" height="36" viewBox="0 0 24 24" fill="none" stroke="#fff" stroke-width="1.8"><rect x="3" y="3" width="14" height="9" rx="2"/><path d="M10 22v-9a1.5 1.5 0 0 1 3 0v4h4a2 2 0 0 1 2 2v3"/><path d="M20 4v6"/></svg>
    </span></div>
    <h3>Subscriptions</h3>
    <p>Lorem ipsum dolor sit amet, consectetur adipiscing elit, sed do et dolore magna aliqua.</p>
    <div class="read-link">Read More &#10140;</div>
  </div>

  <div class="svc-card" style="left:784px">
    <div class="svc-icon"><span>
      <svg width="38" height="38" viewBox="0 0 24 24" fill="none" stroke="#fff" stroke-width="1.8"><rect x="2" y="3" width="20" height="14" rx="1"/><path d="M8 21h8M12 17v4M6 8h5M6 11h5"/><circle cx="16" cy="9" r="2"/></svg>
    </span></div>
    <h3>Online Courses</h3>
    <p>Lorem ipsum dolor sit amet, consectetur adipiscing elit, sed do et dolore magna aliqua.</p>
    <div class="read-link">Read More &#10140;</div>
  </div>
</section>

<section class="about">
  <div class="about-ring"></div>
  <div class="about-photo" role="img" aria-label="Smiling woman with a headscarf outdoors in warm sunlight"></div>
  <h2>About Us</h2>
  <p style="top:155px">Lorem ipsum dolor sit amet, consectetur adipiscing elit, sed do eiusmod tempor incididunt ut labore et dolore magna aliqua. Ut enim ad minim veniam, quis nostrud exercitation ullamco laboris nisi ut aliquip ex ea commodo consequat.</p>
  <p style="top:301px">Duis aute irure dolor in reprehenderit in voluptate velit esse cillum dolore eu fugiat cupidatat non proident, sunt in culpa qui officia deserunt mollit anim id est laborum.</p>
  <div class="btn" style="left:632px;top:417px;width:133px;height:46px">Read More</div>
</section>

<section class="works">
  <h2 class="heading" style="top:80px">Our Works</h2>
  <div class="dots" style="left:92px;top:153px;width:80px;height:11px"></div>
  <div class="dots" style="left:92px;top:153px;width:11px;height:80px"></div>
  <div class="dots" style="left:1030px;top:575px;width:80px;height:11px"></div>
  <div class="dots" style="left:1099px;top:506px;width:11px;height:80px"></div>

  <div class="work-card" style="left:111px;top:175px;height:462px">
    <div class="work-img" role="img" aria-label="Dog sitting on autumn grass beside its owner" style="background:linear-gradient(160deg,#8aa0b8,#7b6a4a 55%,#5d4a30)"></div>
    <h3>Reiki Practitioner</h3>
    <p style="top:267px">Duis aute irure dolor in reprehenderit in voluptate velit esse cillum dolore ea commodo consequat eu fugiat nulla pariatur.</p>
    <div class="btn" style="left:85px;top:389px;width:133px;height:46px">Read More</div>
  </div>

  <div class="work-card" style="left:448px;top:209px;height:460px">
    <div class="work-img" role="img" aria-label="Practitioner treating a client lying on a therapy table" style="background:linear-gradient(160deg,#c7ccd2,#e4ddd4 55%,#a7b3bf)"></div>
    <h3>Calvera Method<br>Practitioner</h3>
    <p style="top:297px">Duis aute irure dolor in reprehenderit in voluptate velit esse cillum dolore nulla pariatur.</p>
    <div class="btn" style="left:85px;top:389px;width:133px;height:46px">Read More</div>
  </div>

  <div class="work-card" style="left:784px;top:175px;height:462px">
    <div class="work-img" role="img" aria-label="Therapist working on a client's leg in a bright clinic" style="background:linear-gradient(160deg,#eef0ee,#cfdbe6 55%,#7d95b8)"></div>
    <h3>Bowen Therapist</h3>
    <p style="top:267px">Duis aute irure dolor in reprehenderit in voluptate velit esse cillum dolore ea commodo consequat eu fugiat nulla pariatur.</p>
    <div class="btn" style="left:85px;top:389px;width:133px;height:46px">Read More</div>
  </div>
</section>

<section class="testimonials">
  <h2 class="heading" style="top:90px">TESTIMONIALS</h2>

  <div class="arrow-btn" style="left:47px;top:341px"><svg width="14" height="14" viewBox="0 0 24 24" fill="none" stroke="#1f7a3c" stroke-width="3"><path d="M15 5l-7 7 7 7"/></svg></div>
  <div class="arrow-btn" style="left:1124px;top:341px"><svg width="14" height="14" viewBox="0 0 24 24" fill="none" stroke="#1f7a3c" stroke-width="3"><path d="M9 5l7 7-7 7"/></svg></div>

  <div class="t-card" style="left:114px">
    <div class="stars"><svg width="80" height="14" viewBox="0 0 80 14" fill="#f5a623"><g id="st"><path d="M7 0l2 4.6 5 .4-3.8 3.3 1.2 4.9L7 10.6 2.6 13.2l1.2-4.9L0 5l5-.4z"/></g><use href="#st" x="16"/><use href="#st" x="32"/><use href="#st" x="48"/><use href="#st" x="64"/></svg></div>
    <p>Lorem ipsum dolor sit amet, consectetur adipiscing elit, sed do eiusmod tempor incididunt ut labore et dolore magna aliqua ut enim ad minim veniam, quis nostrud exercitation ullamco.</p>
    <div class="t-rule"></div>
    <div class="avatar" role="img" aria-label="Client portrait"></div>
    <div class="t-name">Jordan Ellis</div>
    <div class="t-loc">Florida, United States</div>
  </div>

  <div class="t-card" style="left:446px">
    <div class="stars"><svg width="80" height="14" viewBox="0 0 80 14" fill="#f5a623"><use href="#st"/><use href="#st" x="16"/><use href="#st" x="32"/><use href="#st" x="48"/><use href="#st" x="64"/></svg></div>
    <p>Lorem ipsum dolor sit amet, consectetur adipiscing elit, sed do eiusmod tempor incididunt ut labore et dolore magna aliqua ut enim ad minim veniam, quis nostrud exercitation ullamco.</p>
    <div class="t-rule"></div>
    <div class="avatar" role="img" aria-label="Client portrait"></div>
    <div class="t-name">Jordan Ellis</div>
    <div class="t-loc">Florida, United States</div>
  </div>

  <div class="t-card" style="left:779px">
    <div class="stars"><svg width="80" height="14" viewBox="0 0 80 14" fill="#f5a623"><use href="#st"/><use href="#st" x="16"/><use href="#st" x="32"/><use href="#st" x="48"/><use href="#st" x="64"/></svg></div>
    <p>Lorem ipsum dolor sit amet, consectetur adipiscing elit, sed do eiusmod tempor incididunt ut labore et dolore magna aliqua ut enim ad minim veniam, quis nostrud exercitation ullamco.</p>
    <div class="t-rule"></div>
    <div class="avatar" role="img" aria-label="Client portrait"></div>
    <div class="t-name">Jordan Ellis</div>
    <div class="t-loc">Florida, United States</div>
  </div>
</section>

<footer class="footer">
  <svg width="0" height="0" style="position:absolute"><defs><symbol id="arr" viewBox="0 0 24 24"><path d="M3 10h11V5l8 7-8 7v-5H3z" fill="#fff"/></symbol></defs></svg>

  <h4 style="left:97px">Quick Links</h4>
  <ul class="f-list" style="left:99px">
    <li><svg width="14" height="14"><use href="#arr"/></svg>Home</li>
    <li><svg width="14" height="14"><use href="#arr"/></svg>About Us</li>
    <li><svg width="14" height="14"><use href="#arr"/></svg>Services</li>
    <li><svg width="14" height="14"><use href="#arr"/></svg>Our Works</li>
    <li><svg width="14" height="14"><use href="#arr"/></svg>Testimonials</li>
    <li><svg width="14" height="14"><use href="#arr"/></svg>Contact Us</li>
  </ul>

  <h4 style="left:296px">Other Links</h4>
  <ul class="f-list" style="left:298px">
    <li><svg width="14" height="14"><use href="#arr"/></svg>FAQ</li>
    <li><svg width="14" height="14"><use href="#arr"/></svg>Tems of Use</li>
    <li><svg width="14" height="14"><use href="#arr"/></svg>Privacy Policy</li>
    <li><svg width="14" height="14"><use href="#arr"/></svg>Support Links</li>
    <li><svg width="14" height="14"><use href="#arr"/></svg>Conditions</li>
  </ul>

  <h4 style="left:507px">Contact Us</h4>
  <div class="f-contact" style="top:107px">
    <span class="f-ico"><svg width="16" height="16" viewBox="0 0 24 24"><path d="M12 2a7 7 0 0 0-7 7c0 5 7 13 7 13s7-8 7-13a7 7 0 0 0-7-7zm0 9.5A2.5 2.5 0 1 1 12 6.5a2.5 2.5 0 0 1 0 5z" fill="#000"/></svg></span>
    <span>The Marigold Nook<br>Ontario, Canada</span>
  </div>
  <div class="f-contact" style="top:173px">
    <span class="f-ico"><svg width="16" height="16" viewBox="0 0 24 24"><path d="M2 5h20v14H2z" fill="#000"/><path d="M2 6l10 7 10-7" fill="none" stroke="#fff" stroke-width="1.6"/></svg></span>
    <span>info@marigoldnook.ca</span>
  </div>
  <div class="f-contact" style="top:233px">
    <span class="f-ico"><svg width="16" height="16" viewBox="0 0 24 24"><path d="M6.6 10.8a15 15 0 0 0 6.6 6.6l2.2-2.2a1 1 0 0 1 1-.25 11.4 11.4 0 0 0 3.6.57 1 1 0 0 1 1 1V20a1 1 0 0 1-1 1A17 17 0 0 1 3 4a1 1 0 0 1 1-1h3.5a1 1 0 0 1 1 1c0 1.25.2 2.45.57 3.57a1 1 0 0 1-.25 1z" fill="#000"/></svg></span>
    <span>+1 555 010 0199</span>
  </div>

  <div class="news">
    <h4 style="left:811px">Sign Up To Our Newsletter</h4>
    <p>Lorem ipsum dolor sit amet,consectetur adipiscing elit,adipiscing elit.</p>
    <div class="email-field">Email</div>
    <div class="subscribe">Subscribe</div>
  </div>

  <div class="f-rule"></div>
  <div class="copyright">Copyrights@2025.The Marigold Nook.All Rights Reserved</div>
</footer>

</body>
</html>
```